Poster Title Design

Create a text design concept for a documentary film called:
"The Orchard Beekeepers"
Background should be black, design elements and text should be red and/or white.
Design should be bold and readable from a distance.
Please provide at least 3 alternative concepts per submission.
(No need to include images or illustrations in the design. We only need a text treatment with optional simple graphic lines curves or blocks. There are no existing show logos.)
Please submit concepts centered in frame, 1200 wide x 1000 high jpg.
Thanks!
Good Luck!
- please use solid read and white colors for text and design elements.
- please do not use any fonts in the courier family.
please do not use any script or shadow fonts.
please do not use any other colors than red, white and black.
please avoid using gradients.
no need to include images or illustrations, just need the title text treatment.

```html
<!DOCTYPE html>
<html lang="en">
<head>
<meta charset="utf-8">
<title>The Orchard Beekeepers — Title Treatment</title>
<link rel="stylesheet" href="https://fonts.googleapis.com/css2?family=Almendra:wght@700&display=swap">
<style>
  :root {
    --ink-black: #0c0d0f;
    --backdrop-tone: #131417;
    --title-white: #ffffff;
    --title-red: #ff2a12;
    --ribbon-red: #ff2a12;
    --ribbon-white: #ffffff;
  }
  html, body {
    margin: 0;
    padding: 0;
    width: 1200px;
    height: 1000px;
    overflow: hidden;
    background: var(--ink-black);
  }
  .poster {
    position: relative;
    width: 1200px;
    height: 1000px;
    overflow: hidden;
    background: var(--ink-black);
  }
  .poster-backdrop {
    position: absolute;
    inset: 0;
    background: radial-gradient(ellipse at 40% 40%, var(--backdrop-tone) 0%, var(--ink-black) 75%);
  }
  .title-lockup {
    position: absolute;
    left: 575px;
    top: 465px;
    transform: translate(-50%, -50%) rotate(-33deg) scaleY(1.15);
    white-space: nowrap;
    font-family: "Almendra", serif;
    font-weight: 700;
    font-size: 116px;
    line-height: 1;
    letter-spacing: -2px;
    margin: 0;
  }
  .title-lead { color: var(--title-white); }
  .title-main { color: var(--title-red); }
  .ribbon-curves {
    position: absolute;
    right: 0;
    top: 0;
    width: 220px;
    height: 1000px;
  }
  .ribbon-red { stroke: var(--ribbon-red); fill: none; }
  .ribbon-white { stroke: var(--ribbon-white); fill: none; }
</style>
</head>
<body>
  <main class="poster">
    <div class="poster-backdrop" role="img" aria-label="Soft, out-of-focus dark backdrop"></div>

    <h1 class="title-lockup">
      <span class="title-lead">The Orchard</span>
      <span class="title-main">Beekeepers</span>
    </h1>

    <svg class="ribbon-curves" viewBox="980 0 220 1000" aria-hidden="true">
      <path class="ribbon-red" stroke-width="14" d="M1200 150 C1100 330 1030 600 1040 1000"/>
      <path class="ribbon-red" stroke-width="5" d="M1200 280 C1160 480 1140 720 1150 1000"/>
      <path class="ribbon-white" stroke-width="12" d="M1200 440 C1110 560 1060 780 1070 1000"/>
      <path class="ribbon-white" stroke-width="6" d="M1110 380 C1150 450 1170 600 1175 1000"/>
      <path class="ribbon-red" stroke-width="9" d="M1200 700 C1140 780 1100 880 1095 1000"/>
    </svg>
  </main>
</body>
</html>
```